Copper Kettle Catering
Business Cards and Letterhead
Copper Kettle Catering -
Creative Brief
Use standard fonts
R Danela Forsythe
Chef/Owner
287 W 93rd St FL2 New York, NY 10025
copperkettlecatering@mailbox.example
copperkettlecatering.example

```html
<!DOCTYPE html>
<html lang="en">
<head>
<meta charset="utf-8">
<title>Copper Kettle Catering – Business Card</title>
<link rel="stylesheet" href="https://fonts.googleapis.com/css2?family=Arimo:wght@400;700&display=swap">
<style>
  :root {
    --backdrop: #d6d6d6;
    --card: #3b3b3d;
    --band: #ffffff;
    --band-edge: #d9822b;
    --accent-red: #e8412c;
    --accent-orange: #f08a24;
    --brand-gold: #e9a23b;
    --text-light: #f2f2f2;
    --icon: #e5432f;
  }
  * { margin: 0; padding: 0; box-sizing: border-box; }
  html, body {
    width: 1200px; height: 403px; overflow: hidden;
    background: var(--backdrop);
    font-family: "Arimo", Arial, sans-serif;
  }
  .stage { position: relative; width: 1200px; height: 403px; }

  .card {
    position: absolute; top: 58px;
    width: 552px; height: 302px;
    background: var(--card);
    border-radius: 20px;
    overflow: hidden;
    box-shadow: 0 3px 8px rgba(0,0,0,0.35);
  }
  .card--front { left: 36px; }
  .card--back { left: 626px; }

  .front__band {
    position: absolute; left: 0; top: 14px;
    width: 100%; height: 148px;
  }
  .brand-name {
    position: absolute;
    color: var(--brand-gold);
    font-weight: 700;
    white-space: nowrap;
    letter-spacing: 0.5px;
  }
  .card--front .brand-name {
    left: 0; right: 0; top: 62px; text-align: center;
    font-size: 34px;
  }
  .card--back .brand-name {
    left: 0; right: 0; top: 128px; text-align: center;
    font-size: 40px;
  }

  .identity {
    position: absolute; left: 44px; top: 190px;
    color: var(--text-light); font-size: 13px; line-height: 19px;
  }
  .identity__name { color: var(--accent-red); font-weight: 700; }
  .identity__role { color: var(--accent-orange); font-weight: 700; margin-bottom: 18px; }

  .contact {
    position: absolute; left: 278px; top: 188px;
    list-style: none; color: var(--text-light);
    font-size: 13px;
  }
  .contact__item {
    display: flex; align-items: center; gap: 10px;
    height: 23px;
  }
  .contact__icon { width: 14px; height: 14px; flex: none; }
  .divider {
    position: absolute; left: 262px; top: 190px;
    width: 1px; height: 88px; background: #5a5a5c;
  }
</style>
</head>
<body>
<main class="stage">

  <section class="card card--front" aria-label="Business card front">
    <svg class="front__band" viewBox="0 0 552 148" preserveAspectRatio="none" aria-hidden="true">
      <path d="M0 10 L40 4 L80 12 L130 3 L190 11 L250 2 L310 10 L370 3 L430 12 L490 4 L552 9 L552 138 L500 146 L440 136 L380 145 L320 135 L260 144 L200 136 L140 146 L80 137 L30 145 L0 139 Z"
            fill="var(--band)" stroke="var(--band-edge)" stroke-width="4" stroke-opacity="0.55"/>
    </svg>
    <p class="brand-name">Copper Kettle Catering</p>

    <div class="identity">
      <p class="identity__name">R Danela Forsythe</p>
      <p class="identity__role">Chef/Owner</p>
      <p>287 W 93rd St FL2</p>
      <p>New York, NY 10025</p>
    </div>

    <span class="divider" aria-hidden="true"></span>

    <ul class="contact">
      <li class="contact__item">
        <svg class="contact__icon" viewBox="0 0 14 14" aria-hidden="true"><path d="M3 1 L5 1 L6 4 L4.5 5.5 Q6 8.5 8.5 9.5 L10 8 L13 9 L13 11 Q12 13 10 13 Q1 11 1 3 Q1 1 3 1Z" fill="var(--icon)"/></svg>
        <span>212.555.0147</span>
      </li>
      <li class="contact__item">
        <svg class="contact__icon" viewBox="0 0 14 14" aria-hidden="true"><rect x="3.5" y="1" width="7" height="12" rx="1.5" fill="var(--icon)"/><rect x="5" y="3" width="4" height="6" fill="var(--card)"/></svg>
        <span>212.555.0192</span>
      </li>
      <li class="contact__item">
        <svg class="contact__icon" viewBox="0 0 14 14" aria-hidden="true"><circle cx="7" cy="7" r="7" fill="var(--icon)"/><rect x="3.5" y="4.5" width="7" height="5" fill="#fff"/><path d="M3.5 4.5 L7 7.5 L10.5 4.5" fill="none" stroke="var(--icon)" stroke-width="0.8"/></svg>
        <span>copperkettlecatering@mailbox.example</span>
      </li>
      <li class="contact__item">
        <svg class="contact__icon" viewBox="0 0 14 14" aria-hidden="true"><circle cx="7" cy="7" r="7" fill="var(--icon)"/><circle cx="7" cy="7" r="4" fill="none" stroke="#fff" stroke-width="1"/><path d="M3 7 H11 M7 3 V11" stroke="#fff" stroke-width="0.8"/></svg>
        <span>copperkettlecatering.example</span>
      </li>
    </ul>
  </section>

  <section class="card card--back" aria-label="Business card back">
    <p class="brand-name">Copper Kettle Catering</p>
  </section>

</main>
</body>
</html>
```